Flower delivery business needs sales brochure

I have a courier business that specialises in same-day flower deliveries; I want to make a single page A4 sales brochure (folded to DL) to give to our potential customers.
The company website is petalcouriers.net, this will give an idea of who we are and what we do, as well as some graphics and colours that we use.
When opened, the inside A4 space of the brochure will be a pricelist, so the entire page will be an excel table with delivery locations and prices; we will add the prices ourselves later, so ideally the inside will be a background of some sort that won't obstruct text. Maybe light/transparent flowers and a background colour?
The front of the DL brochure should be mostly a title page, so business name, phone number, a graphic?
The first inside page should relate to our service, there's a lot of info on our website that you could use, so same day delivery, 10:30 and 2:30 pick-up times, established over 10 years ago, air-conditioned vans, delivery to 300+ suburbs.
The back page would be contact details and maybe a summary of the key points of the 'about us' section of the website.

Industry/Entity Type

Business

```html
<!DOCTYPE html>
<html lang="en">
<head>
<meta charset="utf-8">
<title>Petal Couriers – Tri-fold Brochure</title>
<link rel="stylesheet" href="https://fonts.googleapis.com/css2?family=Arimo:wght@400;700&display=swap">
<style>
  :root{
    --green:#5a9e32;
    --green-dark:#3f7f22;
    --green-light:#8cc63f;
    --red:#a3202a;
    --red-text:#c1272d;
    --white:#ffffff;
    --ink:#222222;
    --page:#ece8e2;
    --line:#c9c9c9;
  }
  *{box-sizing:border-box;margin:0;padding:0}
  html,body{width:878px;height:1200px;overflow:hidden;background:var(--page)}
  body{position:relative;font-family:"Arimo",Arial,sans-serif;color:var(--ink)}
  .sheet{position:absolute;left:32px;width:814px;overflow:hidden;background:var(--white);box-shadow:0 2px 6px rgba(0,0,0,.25)}
  .sheet--outside{top:14px;height:576px}
  .sheet--inside{top:606px;height:574px}
  .panel{position:absolute;top:0;height:100%;width:271px;overflow:hidden}
  .panel--left{left:0}
  .panel--mid{left:271px;width:272px}
  .panel--right{left:543px}
  .abs{position:absolute}
  .swoosh{position:absolute;left:0;top:0}
  .tab{position:absolute;height:29px;border:1.5px solid var(--white);border-left:none;border-radius:0 6px 6px 0;
       color:var(--white);font-weight:700;font-size:15px;line-height:27px;padding-left:18px;left:0}
  .tab--solid{background:var(--green-light);border:none;color:var(--white)}
  .tab--red{border-color:var(--white);background:var(--red)}
  .copy{position:absolute;font-size:12.6px;line-height:16.2px;text-align:justify}
  .copy p+p{margin-top:16px}
  .copy--white{color:var(--white)}
  .copy--intro{font-size:11.2px;line-height:13.8px}
  .copy--intro p+p{margin-top:13px}
  .photo{position:absolute}
  .contact{position:absolute;left:0;width:272px;text-align:center;color:var(--white);font-size:11.6px;line-height:15px}
  .contact .strong{font-weight:700;font-size:14px}
  .contact .url{font-weight:700;font-size:13px;margin-top:26px}
  .brand{position:absolute;left:20px;top:492px;display:flex;align-items:center;gap:8px;
         font-size:20px;font-weight:700;color:var(--green-dark)}
  .brand-dot{width:22px;height:22px;border-radius:50%;background:var(--red-text)}
  .brand-url{position:absolute;left:30px;top:540px;font-size:15px;letter-spacing:1px;color:var(--green-dark)}
  .services h3{color:var(--red-text);font-size:12.4px;font-weight:700}
  .services{font-size:11.6px;line-height:14px;color:var(--ink)}
  .services .indent{padding-left:10px;text-align:left}
  .pricelist{position:absolute;left:285px;top:52px;width:244px;border-collapse:collapse;background:var(--white);table-layout:fixed}
  .pricelist th{background:var(--green-light);color:var(--white);font-weight:400;font-size:10px;height:24px;border:1px solid var(--white)}
  .pricelist td{height:24.4px;border:1px solid var(--line)}
  .small{font-size:9.4px;line-height:11.6px;color:var(--white);text-align:justify}
  .small h4{font-size:12px;margin-bottom:14px}
</style>
</head>
<body>

<!-- Outside of brochure -->
<section class="sheet sheet--outside">
  <!-- Left panel: about us -->
  <div class="panel panel--left">
    <svg class="swoosh" width="271" height="576" viewBox="0 0 271 576">
      <rect width="271" height="576" fill="#fff"/>
      <path d="M0 0H271V320C200 290 90 300 0 310Z" fill="var(--green)"/>
      <path d="M0 310C110 295 200 300 271 345V300C200 290 90 300 0 300Z" fill="var(--green-light)"/>
      <path d="M0 322C110 310 200 318 271 370V352C200 318 110 312 0 318Z" fill="var(--green-light)" opacity=".55"/>
      <rect y="562" width="271" height="14" fill="var(--green)"/>
    </svg>
    <div class="tab" style="top:13px;width:236px">ABOUT US</div>
    <div class="copy copy--white" style="left:20px;top:45px;width:235px">
      <p>All our air conditioned vans are specially equipped for the delivery of flowers and are presented to your customer by one of our easily recognizable and professional uniformed drivers.</p>
      <p>Our team works hard to build good long term relationships with all our customers and we understand how important it is for your flowers to be delivered on time and in excellent condition.</p>
      <p>We understand that its not just the gift of flowers, but the emotion that we are transporting!</p>
    </div>
    <div class="photo" role="img" aria-label="Red rose petals and lit red candles on a white surface"
         style="left:0;top:380px;width:240px;height:170px;background:radial-gradient(circle at 55% 55%,#e24a4a 0,#f2b5b5 45%,#ffffff 75%)"></div>
  </div>

  <!-- Bouquet photograph spanning middle and right panels -->
  <div class="photo" role="img" aria-label="Woman holding a colourful tulip bouquet with a same day delivery tag"
       style="left:271px;top:0;width:543px;height:420px;background:linear-gradient(120deg,#d8c8bc 0,#e58a6a 35%,#e8b840 65%,#b9a489 100%)"></div>

  <!-- Middle panel: contact -->
  <div class="panel panel--mid" style="pointer-events:none">
    <svg class="swoosh" width="272" height="576" viewBox="0 0 272 576">
      <path d="M0 250C60 320 160 340 272 350V576H0Z" fill="var(--red)"/>
      <path d="M0 240C60 300 160 330 272 338V352C160 345 60 320 0 262Z" fill="var(--white)"/>
      <path d="M0 262C60 320 160 345 272 352V368C160 362 60 340 0 285Z" fill="var(--green-light)"/>
      <rect y="562" width="272" height="14" fill="var(--green)"/>
    </svg>
    <div class="contact" style="top:400px">
      <div>CONTACT US:</div>
      <div>Operations: <span class="strong">0400 555 127</span></div>
      <div>(9am-5pm Mon-Fri &amp; 9am-3pm Sat)</div>
      <div>Email Us: info@petalcouriers.net</div>
      <div style="margin-top:12px">Postal Address:</div>
      <div>PO Box 4821, Riverton DC , QLD, 4999</div>
      <div class="url">www.petalcouriers.net</div>
    </div>
  </div>

  <!-- Right panel: cover -->
  <div class="panel panel--right">
    <svg class="swoosh" width="271" height="576" viewBox="0 0 271 576">
      <path d="M0 368C80 380 180 400 271 430V576H0Z" fill="#fff"/>
      <path d="M200 420C240 460 262 520 271 576V410Z" fill="var(--green)"/>
      <rect y="562" width="271" height="14" fill="var(--green)"/>
    </svg>
    <div class="brand"><span class="brand-dot"></span>Petal Couriers</div>
    <div class="brand-url">www.petalcouriers.net</div>
  </div>
</section>

<!-- Inside of brochure -->
<section class="sheet sheet--inside">
  <!-- Left panel: services -->
  <div class="panel panel--left">
    <svg class="swoosh" width="271" height="574" viewBox="0 0 271 574">
      <rect width="271" height="574" fill="#fff"/>
      <path d="M0 245C90 225 190 240 271 290V574H0Z" fill="var(--green)"/>
      <path d="M0 240C90 215 190 228 271 275V290C190 240 90 228 0 250Z" fill="var(--green-light)"/>
    </svg>
    <div class="tab tab--solid" style="top:10px;width:253px">OUR SERVICES</div>
    <div class="services abs" style="left:11px;top:48px;width:252px;text-align:justify">
      <h3>Pickup &amp; Delivery Times</h3>
      <p>Our service offers pick-ups twice a day for those florists whose volume requires it:</p>
      <p class="indent">A mid-morning pick-up prior to our depot handover at 11:30 noon</p>
      <p class="indent">An afternoon pickup prior to our second depot handover at 2:30pm</p>
      <p style="margin-top:14px">Most flowers are delivered within 4/5 hours after pick-up. Local (ie within area of pickup location) and timed deliveries are given priority and we can accommodate for special deadlines with prior notice.</p>
    </div>
    <div class="copy copy--white copy--intro" style="left:12px;top:308px;width:158px">Petal Couriers Pty Ltd is a courier company that specializes in the delivery of flowers and gifts.</div>
    <div class="photo" role="img" aria-label="White delivery van beside orange and pink gerbera daisies"
         style="left:12px;top:372px;width:252px;height:80px;background:linear-gradient(90deg,#f4f4f4 0,#e6e6e6 45%,#f2a23a 70%,#e24f80 100%);border-radius:6px"></div>
    <div class="copy copy--white copy--intro" style="left:11px;top:458px;width:252px">
      <p>We offer a same day courier service for the florist &amp; gift retail and wholesale market, and deliver to over 300 suburbs throughout the Brisbane Metropolitan region.</p>
      <p>We have been in the business for over 10 years, and are very focused on delivering the best customer service possible.</p>
    </div>
  </div>

  <!-- Middle panel: pricelist -->
  <div class="panel panel--mid" style="background:var(--red)">
    <div class="tab tab--red" style="top:9px;width:225px">PRICELIST</div>
  </div>
  <table class="pricelist" aria-label="Price list">
    <colgroup><col style="width:69px"><col style="width:113px"><col style="width:62px"></colgroup>
    <thead><tr><th>DELIVERY</th><th>LOCATIONS</th><th>PRICE</th></tr></thead>
    <tbody>
      <tr><td></td><td></td><td></td></tr><tr><td></td><td></td><td></td></tr>
      <tr><td></td><td></td><td></td></tr><tr><td></td><td></td><td></td></tr>
      <tr><td></td><td></td><td></td></tr><tr><td></td><td></td><td></td></tr>
      <tr><td></td><td></td><td></td></tr><tr><td></td><td></td><td></td></tr>
      <tr><td></td><td></td><td></td></tr><tr><td></td><td></td><td></td></tr>
      <tr><td></td><td></td><td></td></tr><tr><td></td><td></td><td></td></tr>
      <tr><td></td><td></td><td></td></tr><tr><td></td><td></td><td></td></tr>
      <tr><td></td><td></td><td></td></tr><tr><td></td><td></td><td></td></tr>
      <tr><td></td><td></td><td></td></tr><tr><td></td><td></td><td></td></tr>
      <tr><td></td><td></td><td></td></tr><tr><td></td><td></td><td></td></tr>
    </tbody>
  </table>

  <!-- Right panel: pricing and surcharges -->
  <div class="panel panel--right">
    <svg class="swoosh" width="271" height="574" viewBox="0 0 271 574">
      <rect width="271" height="574" fill="#fff"/>
      <path d="M0 0H271V240C170 250 80 300 0 350Z" fill="var(--green)"/>
      <path d="M0 350C80 300 170 250 271 240V260C170 268 80 310 0 365Z" fill="var(--green-light)"/>
    </svg>
    <div class="tab" style="top:9px;width:246px">PRICING &amp; SURCHARGES</div>
    <div class="small abs" style="left:11px;top:45px;width:252px">
      <h4>What makes us different ?</h4>
      <p>All price lists are customized for each customer based on location of pickup and volume per week. Please contact us and we will be happy to provide a price list based on the information you provide. Unlike other couriers, our surcharges are kept at an absolute minimum - we don't charge for additional items that accompany an order (eg balloons, chocolates or teddy bears*). We also will not charge for a timed delivery that can be done within the driver's daily run or is provided the day before.</p>
      <p style="margin-top:12px">We will also reimburse our customers for any item lost or damaged whilst in our care**</p>
      <p style="margin-top:12px;padding-left:8px;text-align:left">unless very large or cumbersome<br>terms &amp; conditions apply</p>
    </div>
    <div class="photo" role="img" aria-label="Mixed bouquet of gerberas and daisies in a burlap pot"
         style="left:40px;top:345px;width:200px;height:215px;border-radius:40% 40% 20% 20%;background:radial-gradient(circle at 50% 35%,#e0356e 0,#f2b23a 40%,#c9a77a 70%,#ffffff 90%)"></div>
  </div>
</section>

</body>
</html>
```